Every sort of trades everysortoftrades.ca

Website for company offering Every sort of trades
Welding/Fabrication/Metal repairs/Metal building, Electrical repairs and installations, Plumbing and Heating, Renovations, Flooring, Paiting, and other services

We need a very clean and professional website outlining the many services we have

We would like each type of service to have its own page, with images of those types of services on those pages.

Then in the future, we can update those pages with projects we have done of those types.

Every Sort of Trades . CA

Located in Calgary, Alberta, Canada, offering services Alberta wide

Welding/Fabrication/Repair/Building - Steel and metals
Electrical contractor - Journeyman , small or large projects
Plumbing and Heating
Renovations
Flooring
Painting
Other services - storage, trucking, delivery, etc

business and residential services

Contractor

5+ page

Sans Serif

3176b5
0253a1
85acd3
85abd2
cedeed
ffffff

Must have
• Clean
• Professional
• Easy of updating text and images

```html
<!DOCTYPE html>
<html lang="en">
<head>
<meta charset="utf-8">
<title>Every Sort of Trades</title>
<link rel="stylesheet" href="https://fonts.googleapis.com/css2?family=Barlow:wght@400;500;600&family=Lato:wght@400;700&display=swap">
<style>
:root{
  --blue:#3176b5;
  --navy:#0253a1;
  --sky:#85acd3;
  --sky2:#85abd2;
  --pale:#cedeed;
  --white:#ffffff;
  --ink:#222;
  --grey:#555;
  --footer:#ececec;
  --rule:#d4d4d4;
}
*{box-sizing:border-box;margin:0;padding:0}
html,body{width:710px;height:1200px;overflow:hidden;background:var(--white)}
body{position:relative;font-family:"Barlow",sans-serif;color:var(--ink)}
.abs{position:absolute}

.topbar{left:0;top:0;width:710px;height:19px;background:var(--navy);color:var(--white);font-size:7px;font-family:"Lato",sans-serif}
.topbar .contact{left:68px;top:5px;display:flex;gap:10px;align-items:center}
.topbar .search{left:542px;top:5px;color:#7fa6d0;font-size:6.5px;letter-spacing:.3px}
.topbar .search-icon{left:599px;top:5px}
.topbar .soc{top:2px;width:15px;height:15px;background:#111}
.header{left:0;top:19px;width:710px;height:50px;background:linear-gradient(#fff,#ececec)}
.logo{left:70px;top:18px;color:var(--blue);font-weight:600;font-size:14px;letter-spacing:.6px}
.nav{top:14px;text-align:center;font-size:9px;font-weight:500;color:#222;line-height:1.1}
.nav small{display:block;font-size:6px;font-weight:400;color:#333;margin-top:2px;font-family:"Lato",sans-serif}
.btn{display:flex;align-items:center;justify-content:center;gap:5px;color:var(--white);font-size:9px;font-weight:500;letter-spacing:.3px}
.btn-apply{left:458px;top:13px;width:85px;height:22px;background:var(--blue)}
.btn-login{left:557px;top:13px;width:85px;height:22px;background:var(--navy)}

.hero{left:0;top:69px;width:710px;height:317px;background:linear-gradient(100deg,#3b3128 0%,#c56a2a 22%,#2a5d9a 50%,#1d4c89 75%,#8db4dc 100%)}
.hero-title{left:0;top:146px;width:710px;text-align:center;color:var(--white);font-size:19px;font-weight:500;letter-spacing:.5px}
.hero-sub{left:0;top:170px;width:710px;text-align:center;color:var(--white);font-size:8.5px;font-family:"Lato",sans-serif}
.btn-start{left:312px;top:199px;width:86px;height:22px;background:var(--blue)}
.arrow{width:26px;height:26px;border:1.5px solid var(--white);border-radius:50%;display:flex;align-items:center;justify-content:center}

.cards{left:58px;top:346px;width:594px;height:164px;display:flex}
.card{flex:1;color:var(--white);text-align:center;padding-top:18px}
.card h3{font-size:8.5px;font-weight:500;letter-spacing:.2px}
.card svg{margin:10px auto 8px;display:block}
.card p{font-family:"Lato",sans-serif;font-size:6.3px;line-height:13px;padding:0 18px}
.c1{background:var(--blue)}.c2{background:#3a7dbb}.c3{background:var(--sky)}

.rule{left:58px;width:594px;height:1px;background:var(--rule)}
.section-title{left:0;top:538px;width:710px;text-align:center;font-size:18.5px;font-weight:500}

.tile{top:601px;height:108px;display:flex;align-items:center;justify-content:center}
.tile span{color:var(--white);font-size:11.5px;letter-spacing:.4px;border-top:1px solid var(--white);border-bottom:1px solid var(--white);padding:1px 4px}
.t1{left:0;width:178px;background:linear-gradient(135deg,#8ba8c3,#5b7fa3)}
.t2{left:178px;width:156px;background:linear-gradient(160deg,#3a7bbd,#1d5a9c)}
.t3{left:334px;top:588px;width:220px;height:134px;background:linear-gradient(135deg,#c9d9e8,#a58a63 55%,#e0c13a)}
.t4{left:554px;width:156px;background:linear-gradient(135deg,#7da3c8,#4e7aa8)}
.mini-arrow{width:14px;height:14px;border:1px solid var(--white);border-radius:50%;top:648px;display:flex;align-items:center;justify-content:center}

.about-title{left:59px;top:777px;font-size:12.5px;font-weight:500}
.about-img{left:59px;top:805px;width:150px;height:126px;background:linear-gradient(135deg,#e3c9a9,#b89c82 60%,#8c7a6a)}
.about-text{left:224px;top:809px;width:228px;font-family:"Lato",sans-serif;font-size:7.5px;line-height:12.3px;color:var(--grey);text-align:justify}
.btn-more{left:225px;top:941px;width:70px;height:22px;background:var(--blue)}

.call-title{left:468px;top:774px;font-size:12.5px;font-weight:500}
.call{left:466px;width:186px;height:47px;color:var(--white);padding:8px 0 0 32px}
.call small{display:block;font-size:8px;font-weight:500}
.call b{display:block;font-size:13px;font-weight:400;letter-spacing:.3px}
.call svg{position:absolute;right:28px;top:14px}
.k1{top:800px;background:var(--sky)}.k2{top:847px;background:var(--blue)}.k3{top:893px;background:#3a7cbc}

.footer{left:0;top:980px;width:710px;height:200px;background:var(--footer)}
.f-title{top:992px;font-size:12px;font-weight:500;letter-spacing:.3px}
.links{left:82px;top:1018px;list-style:none;font-family:"Lato",sans-serif;font-size:6.5px;color:#333}
.links li{height:15.2px}
.links li::before{content:"›";margin-right:6px}
.bubble{left:198px;top:1016px;width:130px;height:77px;background:#dedede;border-radius:5px;padding:8px 10px;font-family:"Lato",sans-serif;font-size:6.3px;line-height:12px;color:#666;text-align:justify}
.bubble-tail{left:212px;top:1092px}
.avatar{left:218px;top:1098px;width:28px;height:28px;border-radius:50%;background:linear-gradient(#8a6a4c,#d6b79a)}
.who{left:254px;top:1106px;font-size:7px;font-weight:500;color:var(--blue);line-height:9.5px}
.field{left:370px;width:124px;background:var(--white);border:1px solid #c5c5c5;font-family:"Lato",sans-serif;font-size:6px;color:#333;padding:4px 8px}
.btn-submit{left:370px;top:1119px;width:48px;height:18px;background:var(--sky2);font-size:7px}
.follow{left:529px;top:1014px;font-family:"Lato",sans-serif;font-size:6.5px;color:#222}
.follow div{display:flex;align-items:center;gap:9px;height:21.5px}
.follow i{width:16px;height:16px;display:block}
.copy{left:0;top:1180px;width:710px;height:20px;background:#dcdcdc;text-align:center;font-family:"Lato",sans-serif;font-size:6px;color:#333;line-height:20px;letter-spacing:.3px}
</style>
</head>
<body>

<div class="abs topbar">
  <div class="abs contact">
    <span>&#9647;&nbsp; 1-800 555 0142 &nbsp;|</span>
    <span>&#9993;&nbsp; hello@everysortoftrades.ca</span>
  </div>
  <div class="abs search">SEARCH</div>
  <svg class="abs search-icon" width="9" height="9" viewBox="0 0 10 10"><circle cx="4" cy="4" r="3" fill="none" stroke="#7fa6d0" stroke-width="1.4"/><path d="M6.3 6.3 9 9" stroke="#7fa6d0" stroke-width="1.5"/></svg>
  <div class="abs soc" style="left:613px"></div>
  <div class="abs soc" style="left:630px"></div>
</div>

<div class="abs header">
  <div class="abs logo">EVERYSORTOFTRADES</div>
  <div class="abs nav" style="left:247px">HOME<small>Welcome Text!</small></div>
  <div class="abs nav" style="left:326px">SERVICES<small>Need Help</small></div>
  <div class="abs nav" style="left:391px">CONTACT US<small>Support / Help</small></div>
  <div class="abs btn btn-apply"><svg width="8" height="9" viewBox="0 0 8 9"><rect x=".5" y=".5" width="7" height="8" fill="none" stroke="#fff"/><path d="M2 3h4M2 5h4M2 7h3" stroke="#fff" stroke-width=".8"/></svg>APPLY NOW</div>
  <div class="abs btn btn-login">LOGIN / SIGN UP</div>
</div>

<div class="abs hero" role="img" aria-label="Welder grinding metal with sparks flying, blue workwear"></div>
<div class="abs arrow" style="left:61px;top:224px"><svg width="8" height="12" viewBox="0 0 8 12"><path d="M6 1 1.5 6 6 11" fill="none" stroke="#fff" stroke-width="1.6"/></svg></div>
<div class="abs arrow" style="left:620px;top:224px"><svg width="8" height="12" viewBox="0 0 8 12"><path d="M2 1 6.5 6 2 11" fill="none" stroke="#fff" stroke-width="1.6"/></svg></div>
<div class="abs hero-title">EVERY SORT OF TRADES</div>
<div class="abs hero-sub">Neque porro quisquam est qui dolorem ipsum quia</div>
<div class="abs btn btn-start"><svg width="9" height="9" viewBox="0 0 10 10"><circle cx="5" cy="5" r="5" fill="#fff"/><path d="M4 2.8 6.3 5 4 7.2" fill="none" stroke="#3176b5" stroke-width="1.4"/></svg>GET STARTED</div>

<div class="abs cards">
  <div class="card c1">
    <h3>WELDING / FABRICATION</h3>
    <svg width="46" height="30" viewBox="0 0 46 30"><path d="M2 8l14 6M2 15h14M2 22l14-6M5 4l10 9M5 26l10-9" stroke="#fff" stroke-width="1"/><rect x="20" y="8" width="22" height="18" rx="3" fill="#fff"/><rect x="24" y="12" width="8" height="4" fill="#3176b5"/></svg>
    <p>Lorem ipsum dolor sit amet, consectetur adipiscing elit, sed do eiusmod tempor incididunt ut labore et dolore magna aliqua. Duis aute irure dolor in reprehenderit in voluptate velit...</p>
  </div>
  <div class="card c2">
    <h3>METAL REPAIRS / METAL BUILDING</h3>
    <svg width="46" height="30" viewBox="0 0 46 30"><g fill="none" stroke="#fff" stroke-width="1.6"><path d="M14 27 34 5l5 4-20 22z"/><path d="M14 27l-3 3M34 5l3-4"/><path d="M19 24l16-18" stroke-dasharray="1.5 1.5"/></g></svg>
    <p>Lorem ipsum dolor sit amet, consectetur adipiscing elit, sed do eiusmod tempor incididunt ut labore et dolore magna aliqua. Duis aute irure dolor in reprehenderit in voluptate velit...</p>
  </div>
  <div class="card c3">
    <h3>ELECTRICAL REPAIRS &amp; INSTALLATIONS</h3>
    <svg width="46" height="30" viewBox="0 0 46 30"><g fill="none" stroke="#fff" stroke-width="1.3"><path d="M17 13a6 6 0 1 1 12 0c0 3-3 4-3 8h-6c0-4-3-5-3-8z"/><path d="M20 24h6M21 27h4M23 1v3M13 5l2 2M33 5l-2 2M10 13h3M33 13h3"/></g></svg>
    <p>Lorem ipsum dolor sit amet, consectetur adipiscing elit, sed do eiusmod tempor incididunt ut labore et dolore magna aliqua. Duis aute irure dolor in reprehenderit in voluptate velit...</p>
  </div>
</div>

<div class="abs rule" style="top:534px"></div>
<div class="abs section-title">Our Services</div>

<div class="abs tile t1" role="img" aria-label="Tradesman laying floor boards"><span>FLOORING</span></div>
<div class="abs tile t2" role="img" aria-label="Shower head spraying water"><span>PLUMBING AND HEATING</span></div>
<div class="abs tile t3" role="img" aria-label="Worker with tool belt and hard hat in a room under renovation"><span>RENOVATIONS</span></div>
<div class="abs tile t4" role="img" aria-label="Couple choosing paint colours"><span>PAINTING</span></div>
<div class="abs mini-arrow" style="left:8px"><svg width="5" height="7" viewBox="0 0 5 7"><path d="M4 .5 1 3.5 4 6.5" fill="none" stroke="#fff"/></svg></div>
<div class="abs mini-arrow" style="left:689px"><svg width="5" height="7" viewBox="0 0 5 7"><path d="M1 .5 4 3.5 1 6.5" fill="none" stroke="#fff"/></svg></div>

<div class="abs rule" style="top:756px"></div>

<div class="abs about-title">About Our Company</div>
<div class="abs about-img" role="img" aria-label="Hand tightening a pipe valve with a wrench"></div>
<p class="abs about-text">Sed ut perspiciatis unde omnis iste natus error sit voluptatem accusantium doloremque laudantium, totam rem aperiam, eaque ipsa quae ab illo inventore veritatis et quasi architecto beatae vitae dicta sunt explicabo. Nemo enim ipsam voluptatem quia voluptas sit aspernatur aut odit aut fugit, sed quia consequuntur magni dolores eos qui ratione voluptatem sequi nesciunt. Neque porro quisquam est, qui dolorem ipsum quia dolor sit amet, consectetur, adipisci velit, sed quia non numquam eius modi tempora incidunt ut labore et dolore magnam aliquam quaerat voluptatem.</p>
<div class="abs btn btn-more">READ MORE</div>

<div class="abs call-title">Call &amp; Contact Us</div>
<div class="abs call k1"><small>Appointments</small><b>1-800 555 0178</b>
  <svg width="8" height="13" viewBox="0 0 8 13"><rect x=".7" y=".7" width="6.6" height="11.6" rx="1" fill="none" stroke="#fff" stroke-width="1.2"/><circle cx="4" cy="10.3" r=".7" fill="#fff"/></svg></div>
<div class="abs call k2"><small>Office</small><b>1-800 555 0190</b>
  <svg width="12" height="12" viewBox="0 0 12 12"><path d="M2.5 1l2 2.5-1.2 1.3a7 7 0 0 0 3.9 3.9L8.5 7.5 11 9.5 9.6 11C5 11 1 7 1 2.4z" fill="#fff"/></svg></div>
<div class="abs call k3"><small>Resident Services</small><b>CLICK HERE</b>
  <svg width="11" height="16" viewBox="0 0 11 16"><text x="0" y="15" fill="#fff" font-family="Barlow,sans-serif" font-size="18">?</text></svg></div>

<div class="abs footer"></div>
<div class="abs f-title" style="left:82px">Quick Links</div>
<ul class="abs links">
  <li>Home</li><li>About Us</li><li>Services</li><li>Contact Us</li><li>Apply Now</li><li>Login / Sign Up</li>
</ul>

<div class="abs f-title" style="left:202px">Testimonials</div>
<p class="abs bubble">"Lorem ipsum dolor sit amet, consectetur adipiscing elit, sed do eiusmod tempor incididunt ut labore et dolore magna aliqua. Ut enim ad minim veniam."</p>
<svg class="abs bubble-tail" width="12" height="8" viewBox="0 0 12 8"><path d="M0 0h12L4 8z" fill="#dedede"/></svg>
<div class="abs avatar" role="img" aria-label="Customer portrait"></div>
<div class="abs who">Sam Rivers,<br>Lorium ipsum</div>

<div class="abs f-title" style="left:371px">Contact Us</div>
<div class="abs field" style="top:1017px;height:18px">Name</div>
<div class="abs field" style="top:1043px;height:18px">Email Id</div>
<div class="abs field" style="top:1069px;height:43px">Message</div>
<div class="abs btn btn-submit">Submit</div>

<div class="abs f-title" style="left:529px">Follow Us</div>
<div class="abs follow">
  <div><i style="background:#2f5f9e"></i>Chatterbook</div>
  <div><i style="background:#2aa3e0"></i>Tweetline</div>
  <div><i style="background:#d0312d"></i>ViewTube</div>
  <div><i style="background:#df4a32"></i>Circleplus</div>
</div>

<div class="abs copy">Copyrights © 2017 - All Rights Reserved</div>

</body>
</html>
```